'Cradle Ahead' promotional brochure

We have designed a 6 week program to educate impending first-time parents about the things they need to know to survive the first 6 months. Sessions delivered by general practitioner/family doctor, dietician, physiotherapist, speech pathologist and psychologist. Our promotional blurb is: 'A comprehensive education program for first-time parents-to-be, delivered over 6 weeks by health professionals in your community, about everything you need to know to look after your baby (and yourself!) in the first 6 months'. I now want to put together a promotional brochure to be distributed to those couples who express an interest which will provide further details of what will be delivered in the course.
Updates
In terms of layout, I envisaged a double sided A4 size, foldable into 3 sections, but very happy to be guided on this.
Target Market(s)
To appeal to a young, well educated demographic. First time parents couples.
Industry/Entity Type
Medical
Font styles to use
Other font styles liked:
- Playfair Display
Requirements
Must have
- Playfair display font to be consistent with our logo (attached). Logo also included please. Some consistency with colours of logo please.
Nice to have
- I am a doctor, and have no creative genes! But prefer a clean and professional appearance overall. Not too cluttered in overall appearance.
Should not have
- No cheesy pictures of babies.

```html
<!DOCTYPE html>
<html lang="en">
<head>
<meta charset="utf-8">
<title>Cradle Ahead – Trifold Brochure</title>
<link rel="stylesheet" href="https://fonts.googleapis.com/css2?family=Lato:wght@400;700&family=Montserrat:wght@700&family=Playfair+Display:wght@400&display=swap">
<style>
  :root {
    --green: #6ab23c;
    --green-dark: #58a02c;
    --ink: #3a3a3a;
    --ink-soft: #555555;
    --paper: #ffffff;
    --backdrop: #e4e4e4;
    --mist: #efefef;
    --skin-light: #f3ddd2;
    --skin-mid: #d9b3a1;
  }
  * { box-sizing: border-box; margin: 0; padding: 0; }
  html, body { width: 1200px; height: 764px; overflow: hidden; }
  body {
    background: var(--backdrop);
    font-family: "Lato", Arial, sans-serif;
    color: var(--ink);
  }
  .brochure {
    position: absolute;
    left: 105px; top: 32px;
    width: 990px; height: 700px;
    display: flex;
    background: var(--paper);
    box-shadow: 0 10px 30px rgba(0,0,0,0.15);
  }
  .panel { position: relative; width: 330px; height: 100%; overflow: hidden; }
  .panel + .panel { border-left: 1px solid #e6e6e6; }

  /* Left panel – programme */
  .programme { padding: 26px 30px 0 34px; }
  .week-title {
    font-family: "Lato", Arial, sans-serif; font-weight: 700;
    color: var(--green); font-size: 14px; letter-spacing: 0.5px; margin-bottom: 4px;
  }
  .intro, .session { font-size: 9.5px; line-height: 1.4; color: var(--ink-soft); }
  .session { text-align: justify; margin-bottom: 5px; }
  .session strong { color: var(--ink); }
  .topics { list-style: none; margin: 8px 0 14px; }
  .topics li {
    font-size: 10.5px; line-height: 1.75; color: var(--ink-soft);
    display: flex; align-items: center; gap: 10px;
  }
  .topics svg { width: 10px; height: 8px; flex: none; }
  .left-photo { position: absolute; left: 0; bottom: 0; width: 100%; height: 255px; }
  .left-photo .rule { position: absolute; top: 0; left: 0; width: 100%; height: 5px; background: var(--green); }
  .left-photo .fill {
    position: absolute; top: 5px; left: 0; right: 0; bottom: 0;
    background: radial-gradient(ellipse at 55% 40%, var(--skin-light), var(--skin-mid) 60%, #a6847a);
  }

  /* Middle panel – contact */
  .contact-panel { background: linear-gradient(180deg, #f7f7f7, var(--mist) 60%, #fafafa); }
  .contact-panel .backdrop-photo {
    position: absolute; inset: 0;
    background: radial-gradient(ellipse at 50% 30%, #e2e2e2, #f4f4f4 55%, #fbfbfb);
  }
  .brand {
    display: flex; align-items: center; gap: 10px;
    font-family: "Playfair Display", Georgia, serif; color: var(--ink-soft);
  }
  .brand .dot { width: 16px; height: 16px; border-radius: 50%; background: var(--green); flex: none; }
  .brand-small { position: absolute; top: 70px; left: 0; right: 0; justify-content: center; font-size: 13px; line-height: 1.2; }
  .contact-badge { position: absolute; left: 15px; top: 205px; width: 300px; height: 270px; }
  .contact-list {
    position: absolute; left: 15px; top: 224px; width: 300px;
    list-style: none; text-align: center; color: #fff; font-size: 11.5px;
  }
  .contact-list li { display: flex; flex-direction: column; align-items: center; margin-bottom: 6px; line-height: 1.3; }
  .contact-list svg { width: 13px; height: 13px; margin-bottom: 2px; }

  /* Right panel – cover */
  .cover-head { height: 150px; display: flex; align-items: center; padding-left: 30px; }
  .brand-large { font-size: 22px; line-height: 1.15; }
  .brand-large .dot { width: 34px; height: 34px; }
  .cover-rule { height: 5px; background: var(--green); }
  .cover-photo {
    height: 270px;
    background: radial-gradient(ellipse at 50% 55%, #f8e6dc, #ecc9b8 55%, #f6efea);
  }
  .cover-title {
    position: absolute; left: 0; right: 0; bottom: 0; height: 275px;
    background: var(--green); padding: 48px 0 0 38px;
  }
  .title-top { font-family: "Montserrat", Arial, sans-serif; font-weight: 700; font-size: 42px; color: var(--ink); line-height: 1; }
  .title-main { font-family: "Playfair Display", Georgia, serif; font-size: 70px; color: #fff; line-height: 1.15; letter-spacing: 1px; }
</style>
</head>
<body>
<main class="brochure">

  <section class="panel programme-panel">
    <div class="programme">
      <h3 class="week-title">WEEK 1</h3>
      <p class="intro">GP Dr Maren Holloway will share information for Mum's own health after delivery. Topics include:</p>
      <ul class="topics">
        <li><svg viewBox="0 0 10 8"><path d="M1 4l3 3 5-6" fill="none" stroke="var(--green)" stroke-width="2"/></svg>Vaccinations in pregnancy</li>
        <li><svg viewBox="0 0 10 8"><path d="M1 4l3 3 5-6" fill="none" stroke="var(--green)" stroke-width="2"/></svg>Bleeding, bladder &amp; bowel after delivery</li>
        <li><svg viewBox="0 0 10 8"><path d="M1 4l3 3 5-6" fill="none" stroke="var(--green)" stroke-width="2"/></svg>Breastfeeding, engorgement and mastitis</li>
        <li><svg viewBox="0 0 10 8"><path d="M1 4l3 3 5-6" fill="none" stroke="var(--green)" stroke-width="2"/></svg>Bottle feeding</li>
        <li><svg viewBox="0 0 10 8"><path d="M1 4l3 3 5-6" fill="none" stroke="var(--green)" stroke-width="2"/></svg>Post-natal anxiety &amp; depression</li>
        <li><svg viewBox="0 0 10 8"><path d="M1 4l3 3 5-6" fill="none" stroke="var(--green)" stroke-width="2"/></svg>Intimacy and contraception</li>
      </ul>
      <h3 class="week-title">WEEK 2</h3>
      <p class="session"><strong>Session 1</strong> – Clinical Psychologist Dr Alys Brennan will discuss changes in relationships as couples become parents, gender roles in parenting and post-natal depression.</p>
      <p class="session"><strong>Session 2</strong> – Physiotherapist Tessa Lindqvist will present advice for Mums regarding exercise during and after pregnancy, looking after the pelvic floor during and after pregnancy and abdominal muscle separation management. She will also provide advice for promoting babies' neck strength and minimising the risk of flat spots on the head and encouraging gross motor skills in the first 6 months.</p>
    </div>
    <div class="left-photo">
      <div class="rule"></div>
      <div class="fill" role="img" aria-label="Photo of a newborn's feet cradled in a parent's hands"></div>
    </div>
  </section>

  <section class="panel contact-panel">
    <div class="backdrop-photo" role="img" aria-label="Faded black and white photo of a parent holding a sleeping baby"></div>
    <div class="brand brand-small"><span class="dot"></span><span>Wattlebrook<br>Health &amp; Medical</span></div>
    <svg class="contact-badge" viewBox="0 0 300 270" aria-hidden="true">
      <polygon points="0,20 60,0 240,0 300,20 300,200 150,270 0,200" fill="var(--green)"/>
      <polygon points="10,27 63,10 237,10 290,27 290,194 150,259 10,194" fill="none" stroke="#fff" stroke-width="3"/>
    </svg>
    <ul class="contact-list">
      <li><svg viewBox="0 0 14 14"><path d="M7 1a4.5 4.5 0 0 0-4.5 4.5C2.5 9 7 13 7 13s4.5-4 4.5-7.5A4.5 4.5 0 0 0 7 1zm0 6.2a1.7 1.7 0 1 1 0-3.4 1.7 1.7 0 0 1 0 3.4z" fill="#fff"/></svg>123 Your street,<br>Your town, Pin</li>
      <li><svg viewBox="0 0 14 14"><path d="M3 1.5l2.2 2.6-1.2 1.6c.8 1.7 2.2 3.1 3.9 3.9l1.6-1.2 2.6 2.2-1.3 1.9C6 12.3 1.7 8 1.1 2.8z" fill="#fff"/></svg>123-456-7890</li>
      <li><svg viewBox="0 0 14 14"><rect x="1" y="3" width="12" height="8" rx="1" fill="#fff"/><path d="M1.5 3.5L7 8l5.5-4.5" fill="none" stroke="var(--green)" stroke-width="1.2"/></svg>hello@wattlebrookhealth.example</li>
      <li><svg viewBox="0 0 14 14"><circle cx="7" cy="7" r="6" fill="none" stroke="#fff" stroke-width="1.4"/><path d="M1 7h12M7 1c-3 3.5-3 8.5 0 12M7 1c3 3.5 3 8.5 0 12" fill="none" stroke="#fff" stroke-width="1.1"/></svg>www.wattlebrookhealth.example</li>
    </ul>
  </section>

  <section class="panel cover-panel">
    <header class="cover-head">
      <div class="brand brand-large"><span class="dot"></span><span>Wattlebrook<br>Health &amp; Medical</span></div>
    </header>
    <div class="cover-rule"></div>
    <div class="cover-photo" role="img" aria-label="Photo of parents' hands forming a heart around a newborn's feet"></div>
    <div class="cover-title">
      <h1>
        <span class="title-top">Cradle</span><br>
        <span class="title-main">AHEAD</span>
      </h1>
    </div>
  </section>

</main>
</body>
</html>
```